Photography Business Card Design

I want a simple,classy design using a logo and simple font such as minion pro or similar. I have attached a logo that I quite like or am open to something similar. On the back of the card I would like the attached photo possibly with my website address on it some where. I want a matt black with silver or grey print. Possibly have the logo off to one side with the words Daniel Pettiford Photography stacked on top of each other
Updates
I am very sorry that some how I forgot to put my facebook address on the details section, www.facenook-social.example/DanielPettifordPhotography
If this could be include on the card as well.
Industry/Entity Type
Business
Contact Information for Business Card
Daniel Pettiford Photography
www.danielpettifordphotography.example.au
Email: danielpettiford@wavelink.example
Phone: +61 (0)492 316 507
Logo Text
Logo styles of interest
Abstract Logo
Look and feel

```html
<!DOCTYPE html>
<html lang="en">
<head>
<meta charset="utf-8">
<title>Daniel Pettiford Photography – Business Card</title>
<link rel="stylesheet" href="https://fonts.googleapis.com/css2?family=Crimson+Pro:wght@400;600&display=swap">
<style>
  :root {
    --canvas-bg: #e6e7e9;
    --card-black: #050505;
    --print-grey: #5b5b5b;
    --print-grey-light: #8a8a8a;
    --photo-light: #8c8c8c;
    --photo-mid: #3c3c3c;
    --photo-dark: #0b0b0b;
  }
  * { margin: 0; padding: 0; box-sizing: border-box; }
  html, body { width: 1200px; height: 1000px; overflow: hidden; }
  body {
    position: relative;
    background: var(--canvas-bg);
    font-family: "Crimson Pro", "Minion Pro", Georgia, serif;
  }
  .card {
    position: absolute;
    width: 661px;
    height: 381px;
    overflow: hidden;
    background: var(--card-black);
    box-shadow: 3px 4px 6px rgba(0, 0, 0, 0.25);
  }
  .card--front { left: 70px; top: 94px; color: var(--print-grey); }
  .card--back { left: 469px; top: 525px; }

  /* Front */
  .brand-mark {
    position: absolute;
    left: 0; right: 0; top: 100px;
    text-align: center;
    font-weight: 600;
    font-size: 22px;
    line-height: 26px;
    color: var(--print-grey);
  }
  .business-name {
    position: absolute;
    left: 0; right: 0; top: 238px;
    text-align: center;
    font-weight: 600;
    font-size: 33px;
    line-height: 40px;
    color: var(--print-grey);
  }
  .contact-list {
    position: absolute;
    left: 0; right: 0; top: 276px;
    list-style: none;
    font-size: 18px;
    line-height: 31px;
    color: var(--print-grey);
  }
  .contact-list li { display: flex; justify-content: center; align-items: center; gap: 6px; }
  .contact-icon { width: 16px; height: 16px; fill: none; stroke: var(--print-grey); stroke-width: 1.6; }
  .contact-icon--solid { fill: var(--print-grey); stroke: none; }

  /* Back */
  .back-photo {
    position: absolute; inset: 0;
    background: linear-gradient(120deg, var(--photo-light) 0%, var(--photo-mid) 35%, var(--photo-dark) 75%);
  }
  .back-mark {
    position: absolute;
    right: 32px; top: 284px;
    width: 110px;
    text-align: center;
    font-size: 11px;
    line-height: 12px;
    color: var(--print-grey-light);
  }
  .back-website {
    position: absolute;
    right: 33px; top: 328px;
    font-size: 16px;
    line-height: 20px;
    color: var(--print-grey-light);
  }
</style>
</head>
<body>
  <section class="card card--front" aria-label="Business card front">
    <div class="brand-mark">Daniel<br>Pettiford<br>Photography</div>
    <h1 class="business-name">Daniel Pettiford Photography</h1>
    <ul class="contact-list">
      <li>
        <svg class="contact-icon" viewBox="0 0 16 16" aria-hidden="true">
          <rect x="1.5" y="3.5" width="13" height="9" rx="1"/>
          <path d="M1.5 4 L8 9 L14.5 4"/>
        </svg>
        danielpettiford@wavelink.example
      </li>
      <li>
        <svg class="contact-icon contact-icon--solid" viewBox="0 0 16 16" aria-hidden="true">
          <path d="M4 1.5 L6.5 1.5 L7 5.5 L5.2 6.5 C5.8 8.5 7 10 9.3 11 L10.3 9.2 L14.5 9.8 L14.5 12.5 C14.5 13.6 13.6 14.5 12.5 14.5 C6.5 14.2 1.8 9.5 1.5 3.5 C1.5 2.4 2.6 1.5 4 1.5 Z"/>
        </svg>
        +61 (0)492 316 507
      </li>
    </ul>
  </section>

  <section class="card card--back" aria-label="Business card back">
    <div class="back-photo" role="img" aria-label="Black and white photograph of a row of pine trees silhouetted against a cloudy sky with the sun shining through"></div>
    <div class="back-mark">Daniel Pettiford<br>Photography</div>
    <p class="back-website">www.danielpettifordphotography.example.au</p>
  </section>
</body>
</html>
```